Holbys Pet Care

Hi. I need a business card /logo for my pet care business. Im thinking about a dogs paw print. Although i do look after other pets so don't want to restrict my self. Open to suggestions on colour etc but like greens and purples.The name of my business is holby's pet care. The logo could be just an image or have holbys power care on it. An option to do either would be great. For the winner i also would like a Web page (word press template if possible) designed if you can, of course I'll pay additional for this. Look forward to your ideas!

```html
<!DOCTYPE html>
<html lang="en">
<head>
<meta charset="utf-8">
<title>Holby's Pet Care – Business Card</title>
<link href="https://fonts.googleapis.com/css2?family=Exo+2:wght@400;500;700;800&display=swap" rel="stylesheet">
<style>
  :root {
    --purple: #7a3a9a;
    --green: #b4e60a;
    --ink: #2e2e33;
    --card: #f7f7f8;
    --backdrop: #e4e4e7;
  }
  * { box-sizing: border-box; margin: 0; padding: 0; }
  html, body { width: 1200px; height: 900px; overflow: hidden; }
  body {
    background: var(--backdrop);
    display: flex; align-items: center; justify-content: center;
    font-family: "Exo 2", sans-serif;
  }
  .business-card {
    position: relative;
    width: 1000px; height: 570px;
    border-radius: 44px;
    background: radial-gradient(circle at 45% 35%, #ffffff 0%, var(--card) 55%, #e9e9ec 100%);
    overflow: hidden;
    box-shadow: 0 10px 30px rgba(0,0,0,.15);
  }
  .card-waves { position: absolute; inset: 0; width: 100%; height: 100%; }
  .brand {
    position: absolute; left: 90px; top: 160px;
    display: flex; align-items: center; gap: 28px;
  }
  .brand-dot { width: 120px; height: 120px; border-radius: 50%; background: var(--purple); }
  .brand-name {
    color: var(--purple); font-weight: 800; font-size: 68px;
    line-height: .92; text-transform: uppercase; letter-spacing: 1px;
  }
  .contact {
    position: absolute; right: 70px; top: 44px;
    text-align: right; color: var(--ink);
  }
  .contact-name { color: var(--purple); font-size: 28px; font-weight: 500; letter-spacing: 2px; text-transform: uppercase; line-height: 1.2; }
  .contact-role { font-size: 20px; font-weight: 500; margin-top: 2px; }
  .contact-address { font-size: 20px; font-weight: 500; margin-top: 26px; line-height: 1.3; }
  .contact-lines { list-style: none; margin-top: 22px; font-size: 16px; line-height: 1.6; }
  .contact-lines li { display: flex; justify-content: flex-end; align-items: center; gap: 10px; }
  .contact-lines svg { width: 16px; height: 16px; fill: var(--purple); flex: none; }
</style>
</head>
<body>
  <article class="business-card">
    <svg class="card-waves" viewBox="0 0 1000 570" preserveAspectRatio="none" aria-hidden="true">
      <path d="M0,430 C350,380 700,430 1000,378 L1000,570 L0,570 Z" fill="var(--green)"/>
      <path d="M0,495 C340,445 700,470 1000,395 L1000,570 L0,570 Z" fill="#ffffff"/>
      <path d="M0,510 C340,460 700,485 1000,406 L1000,570 L0,570 Z" fill="var(--purple)"/>
    </svg>

    <div class="brand">
      <span class="brand-dot"></span>
      <div class="brand-name">Holby's<br>Pet Care</div>
    </div>

    <div class="contact">
      <div class="contact-name">Marcus Delaney</div>
      <div class="contact-role">Managing Director</div>
      <div class="contact-address">14 Fernway Court, Suite 2<br>Brookmill Lane BRK</div>
      <ul class="contact-lines">
        <li>014 552 3098
          <svg viewBox="0 0 24 24"><path d="M6.6 10.8a15 15 0 0 0 6.6 6.6l2.2-2.2c.3-.3.7-.4 1-.2 1.1.4 2.3.6 3.6.6.6 0 1 .4 1 1V20c0 .6-.4 1-1 1A17 17 0 0 1 3 4c0-.6.4-1 1-1h3.5c.6 0 1 .4 1 1 0 1.3.2 2.5.6 3.6.1.3 0 .7-.2 1z"/></svg></li>
        <li>014 552 3099
          <svg viewBox="0 0 24 24"><path d="M7 1h10a2 2 0 0 1 2 2v18a2 2 0 0 1-2 2H7a2 2 0 0 1-2-2V3a2 2 0 0 1 2-2zm0 3v14h10V4zm5 15.5a1 1 0 1 0 0 2 1 1 0 0 0 0-2z"/></svg></li>
        <li>014 552 3100
          <svg viewBox="0 0 24 24"><path d="M6 2h9l3 3v5H6zM3 11h18a1 1 0 0 1 1 1v7a1 1 0 0 1-1 1h-3v2H6v-2H3a1 1 0 0 1-1-1v-7a1 1 0 0 1 1-1zm5 6v3h8v-3z"/></svg></li>
        <li>hello@holbyspets.com
          <svg viewBox="0 0 24 24"><path d="M2 5h20v14H2zm2 2v.5l8 5 8-5V7zm0 2.8V17h16V9.8l-8 5z"/></svg></li>
        <li>www.holbyspetcare.com
          <svg viewBox="0 0 24 24"><path d="M12 2a10 10 0 1 0 0 20 10 10 0 0 0 0-20zm6.9 9h-3a15 15 0 0 0-1.3-6 8 8 0 0 1 4.3 6zM12 4c.9 1.3 1.7 3.8 1.9 7h-3.8C10.3 7.8 11.1 5.3 12 4zM9.4 5a15 15 0 0 0-1.3 6h-3a8 8 0 0 1 4.3-6zM5.1 13h3a15 15 0 0 0 1.3 6 8 8 0 0 1-4.3-6zm6.9 7c-.9-1.3-1.7-3.8-1.9-7h3.8c-.2 3.2-1 5.7-1.9 7zm2.6-1a15 15 0 0 0 1.3-6h3a8 8 0 0 1-4.3 6z"/></svg></li>
      </ul>
    </div>
  </article>
</body>
</html>
```